Wine Label for a wine from Tuscany, Italy

We need a wine label for a white and red wine, can be the same label or can be somewhat differentiated with any variation you feel would be good.. These two wines come from Tuscany, Italy. Wine labels from Tuscany Italy tend to be traditional. We are open to traditional looking labels but also more modern, eye catching too. We want to convey a sense of elegance, importance, great wine. I am attaching some examples of labels we like from Tuscany, also a label that was designed for us recently by one of you, which we LOVE. No wine glasses, wine bottles or grapes featured on the label please. We tend to like the white background. No blue please.

Target Market(s)

More women than men purchase wine, but it needs to appeal to both sexes.

Requirements
Must have
• Wine Name: Casa Morel or Casa morel
• Type/Varletal: Rosso Toscano (White is Vermentino)
• Vintage (year): 2018
• That is all the text we want on the label, thanks
Nice to have
• Clean, something that makes someone want to grab this wine bottle off the shelf!
Should not have
• Images of Wine glass, wine bottles, grapes
• Do not use the color blue please.

```html
<!DOCTYPE html>
<html lang="it">
<head>
<meta charset="utf-8">
<title>Casa Morel – Wine Labels</title>
<link rel="stylesheet" href="https://fonts.googleapis.com/css2?family=Cormorant+Garamond:wght@400;600&display=swap">
<style>
  :root {
    --page: #ffffff;
    --ink: #1e1a1b;
    --band-dark: #231f20;
    --paper: #ffffff;
    --mist: #e6e7e9;
    --gold: #d89a2b;
    --light-text: #ffffff;
  }
  * { margin: 0; padding: 0; box-sizing: border-box; }
  html, body {
    width: 1200px;
    height: 1200px;
    overflow: hidden;
    background: var(--page);
  }
  .label-sheet {
    width: 1200px;
    height: 1200px;
    display: flex;
    flex-direction: column;
    align-items: center;
    justify-content: center;
    gap: 92px;
  }
  .label {
    width: 600px;
    height: 462px;
    display: flex;
    flex-direction: column;
    box-shadow: 4px 6px 10px rgba(0, 0, 0, 0.35);
    font-family: "Cormorant Garamond", serif;
    color: var(--ink);
  }
  .label__brand {
    height: 209px;
    display: flex;
    align-items: center;
    justify-content: center;
    gap: 22px;
  }
  .label__body {
    flex: 1;
    display: flex;
    flex-direction: column;
    align-items: center;
    justify-content: center;
    padding-bottom: 20px;
  }
  .brand-name {
    font-weight: 400;
    font-size: 50px;
    letter-spacing: 0.16em;
    text-transform: uppercase;
    line-height: 1;
  }
  .brand-dot {
    width: 18px;
    height: 18px;
    border-radius: 50%;
    background: var(--gold);
  }
  .wine-type {
    font-weight: 600;
    font-size: 31px;
    letter-spacing: 0.16em;
    line-height: 1;
  }
  .vintage {
    font-weight: 600;
    font-size: 19px;
    letter-spacing: 0.14em;
    margin-top: 6px;
    font-variant-numeric: oldstyle-nums;
  }
  /* Rosso */
  .label--rosso .label__brand { background: var(--band-dark); }
  .label--rosso .brand-name { color: var(--light-text); }
  .label--rosso .label__body { background: var(--paper); }
  /* Bianco */
  .label--bianco .label__brand { background: var(--paper); }
  .label--bianco .brand-name { color: var(--ink); }
  .label--bianco .label__body { background: var(--mist); }
</style>
</head>
<body>
  <main class="label-sheet">
    <section class="label label--rosso">
      <div class="label__brand">
        <span class="brand-name">Casa Morel</span>
        <span class="brand-dot"></span>
      </div>
      <div class="label__body">
        <p class="wine-type">Rosso Toscano</p>
        <p class="vintage">2018</p>
      </div>
    </section>
    <section class="label label--bianco">
      <div class="label__brand">
        <span class="brand-name">Casa Morel</span>
        <span class="brand-dot"></span>
      </div>
      <div class="label__body">
        <p class="wine-type">Vermentino</p>
        <p class="vintage">2018</p>
      </div>
    </section>
  </main>
</body>
</html>
```